This book will apply the 12 Steps to gaming addiction, also known as video game addiction. The primary purpose of the book is to provide an effective solution for this new type of addiction. The solution is based on the rich and successful concepts of traditional twelve-step programs like RL.

The title on the cover will be "Nine Doors Past the Glowing Screen" and "by Martin Quorby". A subtitle can be used if it works in your design of "A Practical Path Beyond Compulsive Console Play". Cover will be for a 6" x 9" book approximately 110 pages in length.

Some back cover text including some review quotes and an author bio are in the attached Word doc. There is also an author photo attached for for the back cover.

Requirements
Must have
• For the cover design it could be stylized, or an image, a partial image, or whatever. I am open to suggestions. Think about what would be noticed by a person searching for help with moderating their video game use, or by the parents or loved ones of problem gamers. Something contemporary and eye catching.

```html
<!DOCTYPE html>
<html lang="en">
<head>
<meta charset="utf-8">
<title>Nine Doors Past the Glowing Screen — Book Cover</title>
<link rel="stylesheet" href="https://fonts.googleapis.com/css2?family=Black+Ops+One&family=Montserrat:wght@300;700&family=Arimo:wght@400;700&family=Cinzel:wght@500&display=swap">
<style>
  :root {
    --bg: #e8e4de;
    --navy-deep: #062a4a;
    --navy: #0b3a63;
    --glow: #3f9fd8;
    --glow-soft: #7cc3ea;
    --spine: #06253f;
    --white: #ffffff;
    --red: #e8312a;
    --body-text: #e6eef6;
  }
  * { margin: 0; padding: 0; box-sizing: border-box; }
  html, body { width: 1200px; height: 800px; overflow: hidden; }
  body { background: var(--bg); position: relative; }

  .cover-wrap {
    position: absolute; left: 100px; top: 40px;
    width: 1000px; height: 720px;
    display: flex;
    box-shadow: 0 10px 30px rgba(0,0,0,.25);
  }

  /* Back cover */
  .back-cover {
    width: 480px; height: 720px; position: relative;
    background:
      radial-gradient(ellipse 55% 28% at 90% 42%, rgba(63,159,216,.4), transparent 70%),
      linear-gradient(180deg, var(--navy) 0%, var(--navy-deep) 100%);
    color: var(--body-text);
    font-family: "Arimo", Arial, sans-serif;
    padding: 44px 40px 0;
  }
  .praise-heading {
    font-family: "Montserrat", Arial, sans-serif;
    font-weight: 700; font-size: 19px; line-height: 1.3;
    text-align: center; color: var(--white); letter-spacing: .5px;
    margin-bottom: 16px;
  }
  .review { font-size: 9.5px; line-height: 1.38; text-align: center; margin-bottom: 10px; }
  .review-source { display: block; font-weight: 700; }
  .blurb { font-size: 9.5px; line-height: 1.38; margin-bottom: 10px; }
  .blurb:first-of-type { margin-top: 22px; }
  .author-block { display: flex; gap: 14px; align-items: flex-start; margin-top: 18px; }
  .author-photo { width: 70px; height: 82px; flex: none; }
  .author-bio { font-size: 9.5px; line-height: 1.38; }

  /* Spine */
  .spine {
    width: 40px; height: 720px;
    background: linear-gradient(90deg, var(--spine), var(--navy-deep) 50%, var(--spine));
  }

  /* Front cover */
  .front-cover {
    width: 480px; height: 720px; position: relative; overflow: hidden;
    background:
      radial-gradient(ellipse 75% 40% at 55% 38%, rgba(124,195,234,.75), transparent 72%),
      radial-gradient(ellipse 60% 30% at 20% 70%, rgba(63,159,216,.45), transparent 70%),
      linear-gradient(180deg, var(--navy) 0%, #11568f 40%, #0c4474 70%, var(--navy-deep) 100%);
  }
  .cover-photo { position: absolute; left: 30px; top: 230px; width: 440px; height: 490px; }
  .book-title {
    position: absolute; left: 0; right: 0; top: 38px;
    font-family: "Black Ops One", Impact, sans-serif;
    text-align: center; color: var(--white);
    font-weight: 400; line-height: .98; font-size: 50px;
    text-shadow: 0 2px 6px rgba(0,0,0,.35);
  }
  .book-title span { display: block; }
  .book-title .title-accent { color: var(--red); font-size: 66px; }
  .subtitle {
    position: absolute; right: 30px; top: 410px; width: 300px;
    font-family: "Montserrat", Arial, sans-serif; font-weight: 300;
    font-size: 18px; line-height: 1.4; letter-spacing: 1.5px;
    color: var(--white); text-align: right;
    text-shadow: 0 1px 5px rgba(0,0,0,.7);
  }
  .author-name {
    position: absolute; right: 30px; bottom: 44px;
    font-family: "Cinzel", Georgia, serif; font-weight: 500;
    font-size: 42px; letter-spacing: 3px; color: var(--white);
    text-shadow: 0 2px 6px rgba(0,0,0,.6);
  }
</style>
</head>
<body>
  <div class="cover-wrap">
    <section class="back-cover">
      <h2 class="praise-heading">Praise for Nine Doors<br>Past the Glowing Screen</h2>

      <p class="review">“A must-read for anyone who is addicted to or thinks they may have a problem with digital gaming. This eloquent work will also be useful to academics and clinicians exploring potential solutions. The author recognizes the similarities between gaming addiction and other addictions, and logically applies one of the most effective known solutions for addiction - The Twelve Steps.”
        <span class="review-source">– Dale Wintermoor, Noted Interventionist and Keynote Speaker</span></p>

      <p class="review">“If you suffer from digital gaming addiction, I strongly encourage you to use this book as your road map to get you back to the real world.”
        <span class="review-source">– Tobias Renquist, Founder of Feedline Review.</span></p>

      <p class="review">“As a high school teacher for 24 years, husband, father, coach, and 12-Step member, I can assure you that this book will transform the life of anyone who is addicted to video games. Well written, easy to understand, and a wonderful book that will provide you with a clear road map to recovery, and this includes teenagers, a group I have been working with in the classroom for decades.”
        <span class="review-source">– Gordon Ellery, Harbor Vale, OR High School Teacher.</span></p>

      <p class="blurb">An effective solution to the challenge of Digital Gaming Addiction (aka Video Game Addiction) based on the rich and successful tradition of the Twelve Steps.</p>
      <p class="blurb">Addiction to Digital Gaming is a new and troubling phenomenon that has burst upon an unprepared society with alarming speed. Many people crave the use of Digital Games in a strikingly similar way to any other addict. Digital Games are a complex software and hardware system that have been designed to promote continued and progressive usage. This sophisticated technology clearly feeds on natural addictive tendencies.</p>
      <p class="blurb">The 12 Steps are one of the most effective methods for treating addiction in human history. Originating with Recovery League in 1939, the 12 Steps have since been used to treat a variety of other addictions, including drugs, sex, gambling, eating disorders, and many others. Now in this groundbreaking work the 12 Steps are applied to the complex and evolving contemporary phenomenon of Digital Gaming Addiction.</p>

      <div class="author-block">
        <svg class="author-photo" role="img" aria-label="Author portrait photograph" viewBox="0 0 70 82">
          <defs><linearGradient id="portraitTone" x1="0" y1="0" x2="0" y2="1"><stop offset="0" stop-color="#8a9a6a"/><stop offset="1" stop-color="#2b3340"/></linearGradient></defs>
          <rect width="70" height="82" fill="url(#portraitTone)"/>
        </svg>
        <p class="author-bio">Marty Quorby is a Technology Consultant and Writer with many years of professional coding and consulting experience. He also struggled with addiction to drugs and alcohol and is now clean and sober in a Twelve-Step program for over 17 years. This unique combination of 12-Step experience and technology expertise led him to create Nine Doors Past the Glowing Screen.</p>
      </div>
    </section>

    <div class="spine"></div>

    <section class="front-cover">
      <svg class="cover-photo" role="img" aria-label="Photo of an intense young gamer with long dreadlocks in a grey hoodie and jeans, crouched on a wooden chair gripping a game controller, with blue smoke and electric sparks" viewBox="0 0 440 490" preserveAspectRatio="none">
        <defs>
          <linearGradient id="photoTone" x1="0" y1="0" x2="0" y2="1">
            <stop offset="0" stop-color="#8a6a4c"/>
            <stop offset=".28" stop-color="#5d5a5e"/>
            <stop offset=".55" stop-color="#4a4c55"/>
            <stop offset=".75" stop-color="#24406a"/>
            <stop offset="1" stop-color="#0a2f52"/>
          </linearGradient>
          <radialGradient id="photoFade" cx="52%" cy="48%" r="58%">
            <stop offset=".55" stop-color="#fff"/>
            <stop offset="1" stop-color="#000"/>
          </radialGradient>
          <mask id="photoMask"><rect width="440" height="490" fill="url(#photoFade)"/></mask>
        </defs>
        <rect width="440" height="490" fill="url(#photoTone)" mask="url(#photoMask)"/>
      </svg>

      <h1 class="book-title">
        <span>NINE DOORS</span>
        <span>PAST THE</span>
        <span class="title-accent">GLOWING</span>
        <span>SCREEN</span>
      </h1>

      <p class="subtitle">A Practical Path Beyond Compulsive Console Play</p>
      <p class="author-name">MARTIN QUORBY</p>
    </section>
  </div>
</body>
</html>
```